TR Pembury, LLC Business Card

I want a two-sided business card that provides people with our contact information, our mission, and a sample of our services. I would love a QR code somewhere on the card linking to our website if possible (www.trpemburyco.com).
Mission:
To help social service organizations develop a Mission Aligned Data Driven mindset that promotes positive change in the lives of the customers they serve.
Services:
Consulting
Training
Community Assessment Development
Strategic Planning
Report Development
Data Analytics
(Note: the website domain is currently mid-transfer so you can't see it at the link we want on the card. You can, however, view it for reference at https://trpemburyco.examplesite.com/)
Contact Information for Business Card
Name: Derek Pembury, NCRT/MT
Title: Chief Executive Officer
Address: 4817 Tallis Lane, Cumming, Georgia 30028
Telephone: (706) 555-0184
Email: derek@trpemburyco.com
Colors
Designer to choose colors to be used in the design.

```html
<!DOCTYPE html>
<html lang="en">
<head>
<meta charset="utf-8">
<title>TR Pembury, LLC Business Card</title>
<link href="https://fonts.googleapis.com/css2?family=Arimo:wght@400;700&family=Noto+Serif:wght@400;700&display=swap" rel="stylesheet">
<style>
  :root {
    --page: #ffffff;
    --card: #dcdddd;
    --brand-blue: #5ba7d9;
    --accent-teal: #4dbdd6;
    --ink-dark: #3a3838;
    --logo-grey: #5b5656;
    --band-start: #151515;
    --band-end: #7a7a7a;
    --band-text: #ffffff;
  }
  * { margin: 0; padding: 0; box-sizing: border-box; }
  html, body { width: 1200px; height: 600px; overflow: hidden; background: var(--page); }
  .canvas { position: relative; width: 1200px; height: 600px; }
  .card {
    position: absolute; top: 160px; width: 500px; height: 285px;
    background: var(--card); border-radius: 22px; overflow: hidden;
  }
  .card--front { left: 92px; }
  .card--back { left: 616px; }

  .front-brand {
    position: absolute; left: 118px; top: 120px;
    display: flex; align-items: center; gap: 12px;
  }
  .brand-dot { width: 34px; height: 34px; border-radius: 50%; background: var(--logo-grey); }
  .front-brand__name {
    font-family: "Arimo", Arial, sans-serif; font-weight: 700;
    font-size: 31px; color: var(--brand-blue); letter-spacing: 0.5px;
  }

  .back-brand {
    position: absolute; right: 14px; top: 22px;
    font-family: "Arimo", Arial, sans-serif; font-weight: 700;
    font-size: 20px; color: var(--accent-teal); letter-spacing: 0.3px;
  }
  .holder { position: absolute; left: 9px; top: 100px; }
  .holder__name {
    font-family: "Noto Serif", Georgia, serif; font-weight: 700;
    font-size: 18px; color: var(--accent-teal); line-height: 1.1;
  }
  .holder__title {
    font-family: "Noto Serif", Georgia, serif; font-weight: 700;
    font-size: 9.5px; color: var(--ink-dark); letter-spacing: 0.4px; margin-top: 4px;
  }
  .services {
    position: absolute; left: 0; top: 145px; width: 500px; height: 45px;
    background: linear-gradient(90deg, var(--band-start) 0%, var(--band-start) 40%, var(--band-end) 100%);
    display: flex; align-items: flex-start; justify-content: center; gap: 4px;
    padding: 18px 4px 0; list-style: none;
    font-family: "Arimo", Arial, sans-serif; font-size: 9px; color: var(--band-text);
  }
  .services li { display: flex; align-items: flex-start; gap: 2px; text-align: center; line-height: 1.1; }
  .services li::before {
    content: ""; flex: none; width: 8px; height: 8px; border-radius: 50%;
    background: var(--band-text); margin-top: 1px;
  }
  .services__long { display: inline-block; }
  .contact {
    position: absolute; display: flex; align-items: flex-start; gap: 10px;
    font-family: "Arimo", Arial, sans-serif; font-size: 15px; color: var(--ink-dark); line-height: 1.05;
  }
  .contact svg { flex: none; fill: var(--accent-teal); }
  .contact--phone { left: 32px; top: 203px; }
  .contact--email { left: 32px; top: 241px; }
  .contact--web { left: 264px; top: 203px; }
  .contact--address { left: 264px; top: 240px; }
</style>
</head>
<body>
<main class="canvas">
  <section class="card card--front" aria-label="Card front">
    <div class="front-brand">
      <span class="brand-dot"></span>
      <span class="front-brand__name">TR PEMBURY, LLC</span>
    </div>
  </section>

  <section class="card card--back" aria-label="Card back">
    <div class="back-brand">TR PEMBURY, LLC</div>

    <div class="holder">
      <p class="holder__name">Derek Pembury, NCRT/MT</p>
      <p class="holder__title">Chief Executive Officer</p>
    </div>

    <ul class="services">
      <li>Consulting</li>
      <li>Training</li>
      <li><span class="services__long">Community Assessment<br>Development</span></li>
      <li>Strategic Planning</li>
      <li>Report Development</li>
      <li>Data Analytics</li>
    </ul>

    <div class="contact contact--phone">
      <svg width="18" height="18" viewBox="0 0 24 24" aria-hidden="true"><path d="M6.6 10.8a15.2 15.2 0 0 0 6.6 6.6l2.2-2.2a1 1 0 0 1 1-.25 11.4 11.4 0 0 0 3.6.57 1 1 0 0 1 1 1V20a1 1 0 0 1-1 1A17 17 0 0 1 3 4a1 1 0 0 1 1-1h3.5a1 1 0 0 1 1 1c0 1.25.2 2.45.57 3.57a1 1 0 0 1-.25 1z"/></svg>
      <span>(706) 555-0184</span>
    </div>
    <div class="contact contact--email">
      <svg width="20" height="14" viewBox="0 0 20 14" aria-hidden="true"><path d="M0 0h20v14H0z M1.5 1.5 10 8l8.5-6.5 M1.5 12.5l6-5 M18.5 12.5l-6-5" fill="var(--accent-teal)" stroke="var(--card)" stroke-width="1.3"/></svg>
      <span>derek@trpemburyco.com</span>
    </div>
    <div class="contact contact--web">
      <svg width="18" height="18" viewBox="0 0 20 20" aria-hidden="true"><g fill="none" stroke="var(--accent-teal)" stroke-width="1.6"><circle cx="10" cy="10" r="8.5"/><ellipse cx="10" cy="10" rx="4" ry="8.5"/><path d="M1.5 10h17M3 5.5h14M3 14.5h14"/></g></svg>
      <span>www.trpemburyco.com</span>
    </div>
    <div class="contact contact--address">
      <svg width="16" height="22" viewBox="0 0 16 22" aria-hidden="true"><path d="M8 0a8 8 0 0 1 8 8c0 5.5-8 14-8 14S0 13.5 0 8a8 8 0 0 1 8-8zm0 5a3 3 0 1 0 0 6 3 3 0 0 0 0-6z"/></svg>
      <span>4817 Tallis Lane, Cumming,<br>Georgia 30028</span>
    </div>
  </section>
</main>
</body>
</html>
```